Gaming Headset Packaging Design

We would like a gaming window box style packaging design for our gaming headset.

We want to use the packaging for 2-3 of our gaming headphone series and hence we would not like to put any product pictures on the packaging.

Size: (enclosed die-cut drawing) please feel free to modify the shape of the window
Material: E Flute Paper box
Type: Window Box style
Design features we prefer: gaming, playful, creative, trendy, High tech.
Requirement: AI file is preferred

Enclosed are a detailed description along with competitor designs and existing die-cut drawing (AI format) for your reference.

Any further questions, please feel free to ask.

```html
<!DOCTYPE html>
<html lang="en">
<head>
<meta charset="utf-8">
<title>Pro Gaming Headset 7.1 – Window Box Dieline</title>
<link rel="stylesheet" href="https://fonts.googleapis.com/css2?family=Oswald:wght@500;600&family=Roboto+Condensed:wght@400;700&display=swap">
<style>
  :root {
    --shelf-red: #ec1c24;
    --header-shadow: #b5161c;
    --band-grey: #c9c9cb;
    --ink: #231f20;
    --white: #ffffff;
    --cut-line: #4fb3e8;
    --paper: #ffffff;
  }
  html, body {
    margin: 0;
    padding: 0;
    width: 1200px;
    height: 900px;
    overflow: hidden;
    background: var(--paper);
  }
  .dieline { display: block; width: 1200px; height: 900px; }
  .fold { fill: none; stroke: var(--cut-line); stroke-width: 1; stroke-dasharray: 3 3; }
  .panel-red { fill: var(--shelf-red); }
  .band { fill: var(--band-grey); }
  .window { fill: var(--white); stroke: var(--cut-line); stroke-width: 1; }
  .flap-open { fill: var(--white); stroke: var(--cut-line); stroke-width: 1; }
  .product-name { font-family: "Oswald", sans-serif; font-weight: 600; fill: var(--ink); font-size: 36px; }
  .product-tagline { font-family: "Oswald", sans-serif; font-weight: 600; fill: var(--white); font-size: 13px; letter-spacing: 0.3px; }
  .features-heading { font-family: "Oswald", sans-serif; font-weight: 600; fill: var(--shelf-red); font-size: 17px; letter-spacing: 0.5px; }
  .feature-text { font-family: "Oswald", sans-serif; font-weight: 500; fill: var(--ink); font-size: 13px; }
  .tick-ring { fill: none; stroke: var(--ink); stroke-width: 2; }
  .tick-mark { fill: none; stroke: var(--shelf-red); stroke-width: 2.6; stroke-linecap: round; stroke-linejoin: round; }
  .spec-box { fill: var(--shelf-red); stroke: var(--header-shadow); stroke-width: 1; }
  .spec-rule { stroke: var(--ink); stroke-width: 0.6; }
  .spec-head { font-family: "Roboto Condensed", sans-serif; font-weight: 700; fill: var(--ink); font-size: 6px; }
  .spec-line { font-family: "Roboto Condensed", sans-serif; fill: var(--ink); font-size: 5.4px; }
  .code-frame { fill: none; stroke: var(--header-shadow); stroke-width: 1; }
  .code-corner { fill: none; stroke: var(--ink); stroke-width: 0.8; }
  .legend-swatch { fill: var(--shelf-red); }
  .legend-text { font-family: "Roboto Condensed", sans-serif; font-weight: 700; fill: var(--ink); font-size: 12px; }
</style>
</head>
<body>
<svg class="dieline" viewBox="0 0 1200 900" xmlns="http://www.w3.org/2000/svg">
  <defs>
    <g id="product-title">
      <text class="product-name" x="238" y="208" textLength="174" lengthAdjust="spacingAndGlyphs">PRO GAMING</text>
      <text class="product-name" x="238" y="243" textLength="174" lengthAdjust="spacingAndGlyphs">HEADSET 7.1</text>
      <text class="product-tagline" x="238" y="260" textLength="174" lengthAdjust="spacingAndGlyphs">VIRTUAL 7.1 SURROUND SOUND</text>
    </g>
  </defs>

  <!-- Open dust and tuck flaps -->
  <path class="flap-open" d="M228 75 L228 45 Q228 31 242 31 L570 31 Q584 31 584 45 L584 75"/>
  <path class="flap-open" d="M30 270 L35 250 L60 163 L216 163 L222 270"/>
  <path class="flap-open" d="M590 270 L590 163 L762 163 L778 250 L780 270"/>
  <path class="flap-open" d="M928 270 L928 242 Q928 235 935 235 L991 235 Q998 235 998 242 L998 305 L928 305 Z"/>
  <path class="flap-open" d="M1142 270 L1190 285 L1190 690 L1142 705"/>

  <!-- Top lid -->
  <rect class="panel-red" x="225" y="75" width="360" height="195"/>

  <!-- Body band -->
  <rect class="band" x="222" y="270" width="920" height="435" role="img" aria-label="Light grey band with a soft triangular tech pattern"/>

  <!-- Left side panel -->
  <rect class="panel-red" x="30" y="270" width="192" height="435"/>

  <!-- Front header -->
  <polygon class="panel-red" points="225,325 502,325 445,382 445,428 225,428"/>
  <!-- Right panel header and spec area -->
  <polygon class="panel-red" points="858,325 1142,325 1142,428 893,428 893,360"/>
  <rect class="spec-box" x="893" y="430" width="249" height="230"/>

  <!-- Display window -->
  <polygon class="window" points="502,325 665,325 658,332 780,332 778,325 858,325 890,357 890,660 760,660 765,650 655,650 648,660 445,660 445,500 458,487 458,395 445,382"/>

  <!-- Fold lines -->
  <line class="fold" x1="225" y1="75" x2="585" y2="75"/>
  <line class="fold" x1="222" y1="270" x2="1142" y2="270"/>
  <line class="fold" x1="30" y1="705" x2="1142" y2="705"/>
  <line class="fold" x1="222" y1="270" x2="222" y2="705"/>
  <line class="fold" x1="585" y1="270" x2="585" y2="705"/>
  <line class="fold" x1="780" y1="270" x2="780" y2="705"/>
  <line class="fold" x1="1142" y1="270" x2="1142" y2="705"/>

  <!-- Bottom flaps -->
  <polygon class="panel-red" points="32,705 222,705 128,790 125,845 40,845 32,838"/>
  <polygon class="panel-red" points="228,705 583,705 583,838 577,845 505,845 500,803 500,845 235,845 228,838"/>
  <polygon class="panel-red" points="590,705 778,705 778,838 772,845 692,845 686,790 590,705"/>
  <polygon class="panel-red" points="782,705 1142,705 1062,790 1060,838 1053,845 874,845 868,838 866,790"/>

  <!-- Titles -->
  <use href="#product-title"/>
  <use href="#product-title" transform="translate(-200,156)"/>
  <use href="#product-title" transform="translate(0,156)"/>
  <use href="#product-title" transform="translate(666,156)"/>

  <!-- Features -->
  <text class="features-heading" x="238" y="481">HEADSET FEATURES:</text>
  <g class="feature-list">
    <g transform="translate(248,503)"><circle class="tick-ring" r="8"/><path class="tick-mark" d="M-4 0 L-1 4 L7 -7"/></g>
    <text class="feature-text" x="267" y="508" textLength="154" lengthAdjust="spacingAndGlyphs">VIRTUAL 7.1 SURROUND SOUND</text>
    <g transform="translate(248,532)"><circle class="tick-ring" r="8"/><path class="tick-mark" d="M-4 0 L-1 4 L7 -7"/></g>
    <text class="feature-text" x="267" y="537" textLength="139" lengthAdjust="spacingAndGlyphs">DUAL DRIVERS ON EACH EAR</text>
    <text class="feature-text" x="267" y="555" textLength="75" lengthAdjust="spacingAndGlyphs">FOR ACCURACY</text>
    <g transform="translate(248,578)"><circle class="tick-ring" r="8"/><path class="tick-mark" d="M-4 0 L-1 4 L7 -7"/></g>
    <text class="feature-text" x="267" y="583" textLength="107" lengthAdjust="spacingAndGlyphs">3D SOUND VIBRATION</text>
    <g transform="translate(248,606)"><circle class="tick-ring" r="8"/><path class="tick-mark" d="M-4 0 L-1 4 L7 -7"/></g>
    <text class="feature-text" x="267" y="611" textLength="140" lengthAdjust="spacingAndGlyphs">BENDABLE STAINLESS-STEEL</text>
    <text class="feature-text" x="267" y="629" textLength="52" lengthAdjust="spacingAndGlyphs">HEADBAND</text>
    <g transform="translate(248,654)"><circle class="tick-ring" r="8"/><path class="tick-mark" d="M-4 0 L-1 4 L7 -7"/></g>
    <text class="feature-text" x="267" y="659" textLength="150" lengthAdjust="spacingAndGlyphs">SOFT AND SOOTHING EARPADS</text>
  </g>

  <!-- Specifications -->
  <g class="spec-table">
    <line class="spec-rule" x1="906" y1="436" x2="906" y2="514"/>
    <line class="spec-rule" x1="1012" y1="436" x2="1012" y2="514"/>
    <text class="spec-head" x="912" y="443">Headphone Specification</text>
    <text class="spec-line" x="912" y="455">Speaker Diameter: Ø40mm</text>
    <text class="spec-line" x="912" y="465">Impedance: 32Ω ± 15%</text>
    <text class="spec-line" x="912" y="475">Sensitivity S.P.L: 113dB ± 3dB</text>
    <text class="spec-line" x="912" y="485">Rated Power: 20mW</text>
    <text class="spec-line" x="912" y="495">Aggregate capability: 30mW</text>
    <text class="spec-line" x="912" y="505">Frequency Response: 20-20kHz</text>
    <text class="spec-line" x="912" y="514">Plug Type: 3.5mm Stereo</text>
    <text class="spec-head" x="1018" y="443">Microphone Specification</text>
    <text class="spec-line" x="1018" y="455">Microphone Unit: Ø6 x 5mm</text>
    <text class="spec-line" x="1018" y="465">Sensitivity: -58dB ± 3dB</text>
    <text class="spec-line" x="1018" y="475">Impedance: &lt;2.2k</text>
    <text class="spec-line" x="1018" y="485">Frequency Response: 30-16kHz</text>
    <text class="spec-line" x="1018" y="495">Standard Operating Voltage: 4.5V</text>
    <text class="spec-line" x="1018" y="505">S/N Ratio: ≥ 58dB</text>
    <text class="spec-line" x="1018" y="514">Plug Type: 3.5mm Stereo</text>
    <text class="spec-line" x="906" y="530">Warning: Adjust headphone sound to a proper volume. Loud sound may damage your ears.</text>
    <text class="spec-line" x="906" y="538">For traffic safety never use the headset while driving.</text>
    <text class="spec-line" x="906" y="550" textLength="226" lengthAdjust="spacingAndGlyphs">Caution: If the user attempts to repair or modify the product in any way we cannot guarantee its performance</text>
    <text class="spec-line" x="906" y="558">of the product. Specifications and design are subject to change without notice for improvements.</text>
  </g>
  <rect class="code-frame" x="906" y="569" width="224" height="80"/>
  <path class="code-corner" d="M918 583 V575 H926 M1002 575 H1010 V583 M918 637 V645 H926 M1002 645 H1010 V637"/>

  <!-- Legend -->
  <rect class="legend-swatch" x="1002" y="155" width="64" height="65"/>
  <text class="legend-text" x="1078" y="178">INSIDE</text>
  <text class="legend-text" x="1078" y="194">SHELF</text>
  <text class="legend-text" x="1078" y="210">COLOR</text>
</svg>
</body>
</html>
```